The Ledgerline Business Card

Business card with QR Code for an accounting and tax business

Target Market(s)

Small Business and Individual Tax

Industry/Entity Type

Bookkeeping, Accounting and Taxes

Contact Information for Business Card

482 CALDWELL ST STE 2210 #614273 BOSTON, MA Zip: 02387

Requirements
Must have
• Name and Address

```html
<!DOCTYPE html>
<html lang="en">
<head>
<meta charset="utf-8">
<title>The Ledgerline Business Card</title>
<link href="https://fonts.googleapis.com/css2?family=Roboto:wght@400;700&display=swap" rel="stylesheet">
<style>
  :root {
    --backdrop: #e4e4e2;
    --card: #f7f7f7;
    --ink: #1c1c1c;
    --muted: #6e6e6e;
    --rule: #3a3a3a;
    --band-dark: #232323;
    --band-light: #8a8a8a;
  }
  * { box-sizing: border-box; margin: 0; padding: 0; }
  html, body {
    width: 1200px; height: 912px; overflow: hidden;
    background: var(--backdrop);
    font-family: "Roboto", Arial, sans-serif;
    color: var(--ink);
  }
  .stage { position: relative; width: 1200px; height: 912px; }
  .card {
    position: absolute; width: 600px; height: 343px;
    background: var(--card);
    box-shadow: 0 6px 18px rgba(0,0,0,0.18);
    overflow: hidden;
  }
  .card--front { left: 80px; top: 60px; }
  .card--back { left: 520px; top: 500px; }

  .brand { display: flex; align-items: center; gap: 12px; }
  .brand__dot {
    width: 44px; height: 44px; border-radius: 50%;
    border: 3px solid var(--ink);
  }
  .brand__name {
    font-weight: 700; font-size: 26px; letter-spacing: 0.5px; color: var(--ink);
  }
  .card--front .brand {
    position: absolute; left: 50%; top: 50%; transform: translate(-50%, -50%);
  }

  .card--back .brand { position: absolute; right: 36px; top: 40px; }
  .card--back .brand__dot { width: 36px; height: 36px; }
  .card--back .brand__name { font-size: 22px; }

  .back__rule-top {
    position: absolute; right: 30px; top: 118px; width: 300px;
    border-top: 1px solid var(--rule);
  }
  .address {
    position: absolute; right: 30px; top: 128px;
    text-align: right; font-size: 14px; line-height: 19px; color: var(--ink);
  }
  .person { position: absolute; left: 30px; top: 196px; }
  .person__name { font-weight: 700; font-size: 24px; line-height: 26px; }
  .person__role { font-size: 15px; color: var(--muted); margin-top: 2px; }
  .person__rule {
    width: 330px; border-top: 1px solid var(--rule); margin: 8px 0 8px;
  }
  .contacts { list-style: none; font-size: 15px; line-height: 21px; }
  .contacts li { display: flex; align-items: center; gap: 8px; }
  .contacts svg { width: 12px; height: 12px; fill: var(--ink); flex: none; }
  .contacts .sep { margin-left: 4px; }

  .band { position: absolute; left: 0; bottom: 0; height: 14px; width: 100%; display: flex; }
  .band__dark { flex: 3; background: var(--band-dark); }
  .band__light { flex: 1; background: var(--band-light); }
</style>
</head>
<body>
<div class="stage">
  <section class="card card--front">
    <div class="brand">
      <span class="brand__dot"></span>
      <span class="brand__name">The Ledgerline</span>
    </div>
  </section>

  <section class="card card--back">
    <div class="brand">
      <span class="brand__dot"></span>
      <span class="brand__name">The Ledgerline</span>
    </div>
    <div class="back__rule-top"></div>
    <address class="address" style="font-style:normal">
      482 Caldwell St<br>
      STE 2210 #614273 Boston<br>
      MA Zip: 02387
    </address>

    <div class="person">
      <div class="person__name">Alan Porter</div>
      <div class="person__role">President</div>
      <div class="person__rule"></div>
      <ul class="contacts">
        <li>
          <svg viewBox="0 0 24 24"><path d="M6.6 10.8a15.1 15.1 0 0 0 6.6 6.6l2.2-2.2a1 1 0 0 1 1-.25 11.4 11.4 0 0 0 3.6.57 1 1 0 0 1 1 1V20a1 1 0 0 1-1 1A17 17 0 0 1 3 4a1 1 0 0 1 1-1h3.5a1 1 0 0 1 1 1c0 1.25.2 2.45.57 3.57a1 1 0 0 1-.25 1z"/></svg>
          <span>(555) 0142-3301</span>
          <svg class="sep" viewBox="0 0 24 24"><path d="M7 1h10a2 2 0 0 1 2 2v18a2 2 0 0 1-2 2H7a2 2 0 0 1-2-2V3a2 2 0 0 1 2-2zm0 3v14h10V4z"/></svg>
          <span>(555) 0142-3302</span>
        </li>
        <li>
          <svg viewBox="0 0 24 24"><path d="M2 5h20v14H2zm2 2v.5l8 5 8-5V7z"/></svg>
          <span>name@theledgerline.com</span>
        </li>
        <li>
          <svg viewBox="0 0 24 24"><circle cx="12" cy="12" r="10"/></svg>
          <span>www.theledgerline.com</span>
        </li>
      </ul>
    </div>

    <div class="band"><span class="band__dark"></span><span class="band__light"></span></div>
  </section>
</div>
</body>
</html>
```